Q7 Labs

I need a business card for my software development company. I have the logo already and will provide that to you. We create web and mobile applications for businesses. I want it to be an edgy design and am thinking (but not required), just the logo on one side and the contact info on the other.

I will upload your finished file to either PrintHarbor or Zib for printing.

Target Market(s)

Business owners who will appreciate an edgy and modern culture in the consultant they hire.

Industry/Entity Type

Software

Requirements
Must have
• Contact info...

Dale Fenwick
President
Dale@q7labs-example.co
http://q7labs-example.co
555.013.4927
@dalefwk
Nice to have
• The address is optional. It's...

2214 Marlow Court
Harborview, VA 23999

Also optional are icons next to the email, twitter, phone and URL to clarify what they are (ex: a twitter icon next to @dalefwk)

```html
<!DOCTYPE html>
<html lang="en">
<head>
<meta charset="utf-8">
<title>Q7 Labs Business Card Fronts</title>
<link rel="stylesheet" href="https://fonts.googleapis.com/css2?family=Quicksand:wght@500;700&display=swap">
<style>
:root{
  --stage:#8c8079;
  --navy:#0f1e5c;
  --navy-deep:#0a1546;
  --silver-light:#f1efea;
  --silver-mid:#d9d6cf;
  --silver-edge:#b9b9bd;
  --white:#ffffff;
  --orange:#e8731c;
  --caption:#ffffff;
}
*{margin:0;padding:0;box-sizing:border-box}
html,body{width:1200px;height:1156px;overflow:hidden}
body{background:var(--stage);font-family:"Quicksand",sans-serif;position:relative}
.card{position:absolute;left:234px;width:676px;overflow:hidden;box-shadow:0 2px 6px rgba(0,0,0,.25)}
.card--plastic{top:46px;height:422px;background:linear-gradient(180deg,var(--silver-light) 0%,var(--silver-mid) 100%);border:1px solid #a9a6a0}
.card--paper{top:584px;height:422px;background:var(--white)}
.card__logo{position:absolute;left:0;right:0;top:70px;display:flex;justify-content:center;align-items:center;gap:14px}
.logo__name{font-weight:700;font-size:72px;color:var(--navy);letter-spacing:1px;line-height:1}
.logo__mark{width:18px;height:18px;background:var(--orange)}
.card__band{position:absolute;left:0;right:0;height:176px;background:linear-gradient(180deg,var(--navy) 0%,var(--navy-deep) 100%);
  border-top:4px solid var(--silver-edge);border-bottom:4px solid var(--silver-edge)}
.card--plastic .card__band{top:214px}
.card--paper .card__band{top:216px}
.card__band::after{content:"";position:absolute;left:0;right:0;bottom:-22px;height:18px;background:linear-gradient(180deg,#c9c9cc,#eeeeee)}
.person{position:absolute;left:66px;top:40px;color:var(--white);font-variant:small-caps;letter-spacing:3px}
.person__name{font-size:22px;font-weight:500}
.person__title{font-size:19px;font-weight:500;margin-left:20px;margin-top:2px}
.divider{position:absolute;left:342px;top:10px;width:2px;height:150px;background:linear-gradient(180deg,transparent,#c8ccd8 50%,transparent)}
.contact{position:absolute;left:380px;top:20px;list-style:none;color:var(--white);font-size:12.5px;letter-spacing:1.6px;font-variant:small-caps;line-height:16px}
.contact li{display:flex;align-items:flex-start;gap:8px;height:22px}
.contact li.contact__address{height:50px}
.contact li.contact__phone{height:26px}
.contact svg{flex:0 0 14px;width:14px;height:14px;margin-top:1px}
.caption{position:absolute;left:0;right:0;text-align:center;color:var(--caption);font-size:29px;font-weight:500;letter-spacing:4px;font-variant:small-caps}
.caption--plastic{top:508px}
.caption--paper{top:1062px}
</style>
</head>
<body>

<section class="card card--plastic" aria-label="Plastic business card front">
  <div class="card__logo"><span class="logo__name">Q7 Labs</span><span class="logo__mark"></span></div>
  <div class="card__band">
    <div class="person"><div class="person__name">Dale Fenwick</div><div class="person__title">President</div></div>
    <div class="divider"></div>
    <ul class="contact">
      <li class="contact__address"><svg viewBox="0 0 14 14"><circle cx="7" cy="7" r="7" fill="#fff"/><path d="M7 3a2.4 2.4 0 0 0-2.4 2.4C4.6 7.3 7 10.8 7 10.8s2.4-3.5 2.4-5.4A2.4 2.4 0 0 0 7 3z" fill="#0f1e5c"/></svg><span>2214 Marlow Court<br>Harborview, VA 23999</span></li>
      <li class="contact__phone"><svg viewBox="0 0 14 14"><circle cx="7" cy="7" r="7" fill="#fff"/><path d="M4.6 3.6l1.4 1.6-.7 1c.5 1 1.2 1.7 2.2 2.2l1-.7 1.6 1.4-.8 1.2C6.6 10.2 3.8 7.4 3.4 4.4z" fill="#0f1e5c"/></svg><span>555.013.4927</span></li>
      <li><svg viewBox="0 0 14 14"><circle cx="7" cy="7" r="7" fill="#fff"/><rect x="3.5" y="4.5" width="7" height="5" fill="none" stroke="#0f1e5c"/><path d="M3.5 4.5L7 7.3l3.5-2.8" fill="none" stroke="#0f1e5c"/></svg><span>Dale@q7labs-example.co</span></li>
      <li><svg viewBox="0 0 14 14"><circle cx="7" cy="7" r="7" fill="#fff"/><circle cx="7" cy="7" r="3.8" fill="none" stroke="#0f1e5c"/><path d="M3.2 7h7.6M7 3.2c-1.6 2.3-1.6 5.3 0 7.6M7 3.2c1.6 2.3 1.6 5.3 0 7.6" fill="none" stroke="#0f1e5c" stroke-width=".8"/></svg><span>http://q7labs-example.co</span></li>
      <li><svg viewBox="0 0 14 14"><circle cx="7" cy="7" r="7" fill="#fff"/></svg><span>@dalefwk</span></li>
    </ul>
  </div>
</section>
<p class="caption caption--plastic">Plastic Business Card Front Size: 3.39” x 2.13</p>

<section class="card card--paper" aria-label="Paper business card front">
  <div class="card__logo"><span class="logo__name">Q7 Labs</span><span class="logo__mark"></span></div>
  <div class="card__band">
    <div class="person"><div class="person__name">Dale Fenwick</div><div class="person__title">President</div></div>
    <div class="divider"></div>
    <ul class="contact">
      <li class="contact__address"><svg viewBox="0 0 14 14"><circle cx="7" cy="7" r="7" fill="#fff"/><path d="M7 3a2.4 2.4 0 0 0-2.4 2.4C4.6 7.3 7 10.8 7 10.8s2.4-3.5 2.4-5.4A2.4 2.4 0 0 0 7 3z" fill="#0f1e5c"/></svg><span>2214 Marlow Court<br>Harborview, VA 23999</span></li>
      <li class="contact__phone"><svg viewBox="0 0 14 14"><circle cx="7" cy="7" r="7" fill="#fff"/><path d="M4.6 3.6l1.4 1.6-.7 1c.5 1 1.2 1.7 2.2 2.2l1-.7 1.6 1.4-.8 1.2C6.6 10.2 3.8 7.4 3.4 4.4z" fill="#0f1e5c"/></svg><span>555.013.4927</span></li>
      <li><svg viewBox="0 0 14 14"><circle cx="7" cy="7" r="7" fill="#fff"/><rect x="3.5" y="4.5" width="7" height="5" fill="none" stroke="#0f1e5c"/><path d="M3.5 4.5L7 7.3l3.5-2.8" fill="none" stroke="#0f1e5c"/></svg><span>Dale@q7labs-example.co</span></li>
      <li><svg viewBox="0 0 14 14"><circle cx="7" cy="7" r="7" fill="#fff"/><circle cx="7" cy="7" r="3.8" fill="none" stroke="#0f1e5c"/><path d="M3.2 7h7.6M7 3.2c-1.6 2.3-1.6 5.3 0 7.6M7 3.2c1.6 2.3 1.6 5.3 0 7.6" fill="none" stroke="#0f1e5c" stroke-width=".8"/></svg><span>http://q7labs-example.co</span></li>
      <li><svg viewBox="0 0 14 14"><circle cx="7" cy="7" r="7" fill="#fff"/></svg><span>@dalefwk</span></li>
    </ul>
  </div>
</section>
<p class="caption caption--paper">Paper Business Card Front Size: 3.39” x 2.13</p>

</body>
</html>
```